Tallwick Haven National Website

We need a website to match our Logo. We will be selling american made vapeing Oils, batteries, Cartomizers, Clearomizers. We have a wharehouse location with couches, TVs streaming clipora, vending machine, and the worlds first flavor mixing bar. We have the lowest priced high grade oils. We will send pictures of the location. Relaxed atmoshpere and no lines for purchase. VIP cards for regulars.

(PLEASE KNOW THAT THE LOGO IS THE UPPER RIGHT LOGO ONLY OF THE FOUR ON THE FILE I ATTACHED)
Updates

Keep in mind we are are only looking for concept and a non coded website

Please know that we are looking for a non coded website

Industry/Entity Type

Purchase

Requirements
Must have
• Online cart, Blog,

```html
<!DOCTYPE html>
<html lang="en">
<head>
<meta charset="utf-8">
<title>Tallwick Haven</title>
<link href="https://fonts.googleapis.com/css2?family=PT+Sans:ital,wght@0,400;0,700;1,400&family=Arimo:wght@400;700&display=swap" rel="stylesheet">
<style>
:root{
  --green:#8dc63f;
  --ink:#ffffff;
  --muted:#d6d6d6;
  --header:#0d0d0d;
  --nav-top:#4a4d4f;
  --nav-bot:#1c1d1e;
  --hero:#eeeded;
  --body:#2d2d2d;
  --card:#444444;
  --card-bar:#1f1f1f;
  --footer:#121212;
}
*{margin:0;padding:0;box-sizing:border-box}
html,body{width:1029px;height:1200px;overflow:hidden;background:var(--body)}
body{position:relative;font-family:"Arimo",Arial,sans-serif;color:var(--ink)}
.abs{position:absolute}
.site-header{left:0;top:0;width:1029px;height:106px;background:linear-gradient(#2a2a2a,var(--header))}
.brand{font-family:"PT Sans",sans-serif;font-size:40px;font-weight:400;color:var(--green);letter-spacing:-0.5px;white-space:nowrap}
.header-brand{left:105px;top:26px}
.social{top:49px;width:31px;height:31px;background:var(--green);border-radius:4px}
.main-nav{left:0;top:111px;width:1029px;height:40px;background:linear-gradient(var(--nav-top),var(--nav-bot));border-top:1px solid #666}
.nav-links{display:flex;align-items:center;list-style:none;font-size:14px;color:#e6e6e6;white-space:nowrap}
.nav-links li{display:flex;align-items:center}
.nav-links .sep{color:#bbb}
.top-links{left:107px;top:122px;gap:0}
.cart{left:791px;top:122px;display:flex;align-items:center;gap:10px;font-size:13px}
.hero{left:0;top:160px;width:1029px;height:260px;background:var(--hero)}
.hero-photo{left:394px;top:160px;width:558px;height:260px;background:linear-gradient(120deg,#cfcfcf,#1b1b1b 40%,#3a3a3a 75%,#dcdcdc)}
.hero-kicker{left:139px;top:212px;font-family:"PT Sans",sans-serif;font-size:25px;color:#111}
.hero-title{left:155px;top:246px;font-family:"PT Sans",sans-serif;font-size:41px;color:var(--green)}
.shop-btn{left:160px;top:318px;width:180px;height:43px;border-radius:10px;background:linear-gradient(#3b3b3b,#111);color:#fff;font-family:"PT Sans",sans-serif;font-size:26px;display:flex;align-items:center;justify-content:center}
.arrow{top:248px;width:32px;height:45px}
.tagline{left:0;top:420px;width:1029px;height:40px;background:linear-gradient(#2e2e2e,#151515);border-bottom:1px solid var(--green);text-align:center;font-family:"PT Sans",sans-serif;font-style:italic;font-size:20px;line-height:40px}
.tagline em{color:var(--green)}
.section-title{font-family:"PT Sans",sans-serif;font-size:19px;color:#eee}
.welcome-title{left:90px;top:495px;font-weight:700}
.intro{left:90px;top:536px;width:584px;font-size:10.3px;line-height:15.4px;color:var(--muted);text-align:justify}
.intro b{color:#fff}
.posts-title{left:90px;top:639px}
.post{left:87px;width:586px;height:142px;background:linear-gradient(#515151,#383838)}
.post-thumb{left:12px;top:23px;width:150px;height:100px;border:1px solid #888;background:linear-gradient(135deg,#4a7f86,#2a3438 55%,#b8377a)}
.post-title{left:175px;top:20px;font-size:14px;font-weight:700;color:var(--green)}
.post-text{left:175px;top:43px;width:398px;font-size:10.3px;line-height:15.4px;color:var(--muted);text-align:justify}
.btn{top:100px;width:98px;height:28px;border-radius:6px;background:linear-gradient(#3a3a3a,#0d0d0d);font-size:10.5px;display:flex;align-items:center;justify-content:center}
.post-meta{left:87px;width:586px;height:31px;background:var(--card-bar);font-size:10.5px;text-align:right;padding-right:11px;line-height:31px}
.post-meta span{color:var(--green)}
.side-title{left:735px}
.product-list{left:745px;top:540px;list-style:none;font-size:14px;color:#e6e6e6}
.product-list li{height:25.7px;display:flex;align-items:center;gap:14px}
.product-list li::before{content:"";border-left:5px solid #ccc;border-top:4px solid transparent;border-bottom:4px solid transparent}
.featured-title{left:735px;top:839px}
.featured-photo{left:738px;top:882px;width:162px;height:154px;background:linear-gradient(135deg,#1c1c1c 30%,#b22222 55%,#e4e4e4)}
.site-footer{left:0;top:1093px;width:1029px;height:107px;background:var(--footer)}
.foot-links{left:90px;top:1121px;font-size:12.5px}
.copyright{left:89px;top:1153px;font-size:10.5px}
.copyright span{color:var(--green)}
.footer-brand{left:749px;top:1130px;font-size:34px;color:#fff}
</style>
</head>
<body>
<header class="site-header abs"></header>
<div class="brand header-brand abs">Tallwick Haven</div>
<span class="social abs" style="left:801px" aria-label="Social link"></span>
<span class="social abs" style="left:844px" aria-label="Social link"></span>

<nav class="main-nav abs"></nav>
<ul class="nav-links top-links abs">
  <li>Home</li><li class="sep" style="margin:0 20px 0 23px">|</li>
  <li>About Us</li><li class="sep" style="margin:0 23px 0 23px">|</li>
  <li>Services</li><li class="sep" style="margin:0 20px 0 27px">|</li>
  <li>Products</li><li class="sep" style="margin:0 30px 0 20px">|</li>
  <li>FAQ</li><li class="sep" style="margin:0 30px 0 26px">|</li>
  <li>Blog</li><li class="sep" style="margin:0 22px 0 24px">|</li>
  <li>Contact Us</li>
</ul>
<div class="cart abs">
  <svg width="22" height="18" viewBox="0 0 22 18"><path d="M1 2h4l3 10h10l3-7H7" fill="none" stroke="#8dc63f" stroke-width="2"/><circle cx="9" cy="15.5" r="1.7" fill="#8dc63f"/><circle cx="17" cy="15.5" r="1.7" fill="#8dc63f"/></svg>
  <span>2 Items</span>
</div>

<section class="hero abs"></section>
<div class="hero-photo abs" role="img" aria-label="Photo of two black electronic cigarettes with a branded box and charger"></div>
<div class="hero-kicker abs">PREMIUM ELECTRONIC</div>
<div class="hero-title abs">CIGARETTES</div>
<div class="shop-btn abs">SHOP NOW</div>
<svg class="arrow abs" style="left:22px" viewBox="0 0 32 45"><rect x="1" y="1" width="30" height="43" fill="#fff" stroke="#555" stroke-width="2"/><path d="M22 6L8 22.5 22 39" fill="none" stroke="#444" stroke-width="6"/></svg>
<svg class="arrow abs" style="left:969px" viewBox="0 0 32 45"><rect x="1" y="1" width="30" height="43" fill="#fff" stroke="#555" stroke-width="2"/><path d="M10 6l14 16.5L10 39" fill="none" stroke="#444" stroke-width="6"/></svg>

<div class="tagline abs">There is no smoke, no ash, no missing out. <em>Just smooth taste you can take anywhere</em></div>

<h2 class="section-title welcome-title abs">Welcome To Our Website</h2>
<p class="intro abs"><b>Lorem Ipsum is simply dummy text of the printing and typesetting industry.</b> Lorem Ipsum has been the industry's standard dummy text ever since the 1500s, when an unknown printer took a galley of type and scrambled it to make a type specimen book. It has survived not only five centuries, but also the leap into electronic typesetting, remaining essentially unchanged men book. It has survived not only five centuries, but also the leap into electronic typesetting, remaining essentially unchanged. men book. It has survived not only five centuries, but also the leap into electronic typesetting, remaining essen</p>

<h2 class="section-title posts-title abs">Latest Posts</h2>

<article class="post abs" style="top:680px">
  <div class="post-thumb abs" role="img" aria-label="Photo of colourful clearomizer tanks in a row"></div>
  <h3 class="post-title abs">E-cigarettes outdo smoking-cessation approaches</h3>
  <p class="post-text abs">Lorem Ipsum is simply dummy text of the printing and typesetting industry. Lorem Ipsum has been the industry's standard dummy text ever since the 1500s, when an unknown printer took a galley of type and scrambled it to make a type specimen book. It has</p>
  <div class="btn abs" style="left:175px">Leave Comment</div>
  <div class="btn abs" style="left:305px">Read More</div>
</article>
<div class="post-meta abs" style="top:822px">Posted 10 hours ago in Class Actions by Mara Quill &nbsp;|&nbsp; <span>0 Comments</span></div>

<article class="post abs" style="top:867px">
  <div class="post-thumb abs" role="img" aria-label="Photo of colourful clearomizer tanks in a row"></div>
  <h3 class="post-title abs">E-cigarettes outdo smoking-cessation approaches</h3>
  <p class="post-text abs">Lorem Ipsum is simply dummy text of the printing and typesetting industry. Lorem Ipsum has been the industry's standard dummy text ever since the 1500s, when an unknown printer took a galley of type and scrambled it to make a type specimen book. It has</p>
  <div class="btn abs" style="left:175px">Leave Comment</div>
  <div class="btn abs" style="left:305px">Read More</div>
</article>
<div class="post-meta abs" style="top:1006px">Posted 10 hours ago in Class Actions by Mara Quill &nbsp;|&nbsp; <span>0 Comments</span></div>

<h2 class="section-title side-title abs" style="top:495px">Our Products</h2>
<ul class="product-list abs">
  <li>With Nicotine</li><li>Without Nicotine</li><li>Batteries</li><li>Usb Charger</li><li>Chargers</li>
  <li>With Nicotine</li><li>Without Nicotine</li><li>Batteries</li><li>Usb Charger</li><li>Chargers</li>
</ul>
<h2 class="section-title featured-title abs">Featured Products</h2>
<div class="featured-photo abs" role="img" aria-label="Photo of a red electronic cigarette kit with charger"></div>

<footer class="site-footer abs"></footer>
<ul class="nav-links foot-links abs">
  <li>Home</li><li class="sep" style="margin:0 20px 0 20px">|</li>
  <li>About Us</li><li class="sep" style="margin:0 20px 0 20px">|</li>
  <li>Services</li><li class="sep" style="margin:0 20px 0 24px">|</li>
  <li>Products</li><li class="sep" style="margin:0 26px 0 20px">|</li>
  <li>FAQ</li><li class="sep" style="margin:0 26px 0 26px">|</li>
  <li>Blog</li><li class="sep" style="margin:0 20px 0 20px">|</li>
  <li>Contact Us</li>
</ul>
<div class="copyright abs">Copyright &nbsp;<span>Tallwick Haven 2013-2014</span></div>
<div class="brand footer-brand abs">Tallwick Haven</div>
</body>
</html>
```